Medical Marijuana Service in the Bay Area

This is for a business card design that is going to be making medical marijuana deliveries in the bay area. The name of the the business is "Coastal Sage Wellness". I would like to have a modern feel and showing us as a medical marijuana company but at the same time discrete about it. I'm trying to target more sophisticated clients.

Industry/Entity Type

Medical

Contact Information for Business Card

Would like people to know it is for medical marijuana but in a discrete way.

```html
<!DOCTYPE html>
<html lang="en">
<head>
<meta charset="utf-8">
<title>Coastal Sage Wellness — Business Card</title>
<link rel="stylesheet" href="https://fonts.googleapis.com/css2?family=Poiret+One&family=Encode+Sans+Semi+Condensed:wght@400&display=swap">
<style>
  :root {
    --page-bg: #ffffff;
    --card-bg: #ffffff;
    --card-edge: #dcdcdc;
    --ink: #555555;
    --wash-yellow: #eef08a;
    --wash-green: #b9dfa8;
    --wash-aqua: #7cc6c8;
    --wash-blue: #2f93b5;
  }
  * { margin: 0; padding: 0; box-sizing: border-box; }
  html, body {
    width: 1200px;
    height: 1000px;
    overflow: hidden;
    background: var(--page-bg);
  }
  .canvas {
    position: relative;
    width: 1200px;
    height: 1000px;
  }
  .business-card {
    position: absolute;
    left: 498px;
    top: 268px;
    width: 264px;
    height: 464px;
    background: var(--card-bg);
    border: 1px solid var(--card-edge);
    display: flex;
    flex-direction: column;
    align-items: center;
  }
  .brand-emblem {
    margin-top: 82px;
    width: 116px;
    height: 116px;
    border-radius: 50%;
    background:
      radial-gradient(circle at 18% 55%, var(--wash-yellow) 0%, rgba(238,240,138,0) 45%),
      radial-gradient(circle at 40% 20%, var(--wash-green) 0%, rgba(185,223,168,0) 50%),
      radial-gradient(circle at 85% 45%, var(--wash-blue) 0%, rgba(47,147,181,0) 60%),
      linear-gradient(100deg, var(--wash-yellow) 0%, var(--wash-green) 30%, var(--wash-aqua) 60%, var(--wash-blue) 100%);
  }
  .brand-name {
    margin-top: 14px;
    font-family: "Poiret One", "Century Gothic", sans-serif;
    font-weight: 400;
    font-size: 23px;
    line-height: 26px;
    color: var(--ink);
    text-align: center;
    letter-spacing: 0.2px;
  }
  .contact {
    margin-top: auto;
    margin-bottom: 28px;
    font-family: "Encode Sans Semi Condensed", "Arial Narrow", sans-serif;
    font-style: normal;
    font-size: 13.5px;
    line-height: 18px;
    color: var(--ink);
    text-align: center;
  }
</style>
</head>
<body>
  <main class="canvas">
    <article class="business-card">
      <div class="brand-emblem" role="img" aria-label="Watercolour wash emblem in yellow, aqua and blue"></div>
      <h1 class="brand-name">Coastal Sage<br>Wellness</h1>
      <address class="contact">
        <p class="contact-phone">415-555-0142</p>
        <p class="contact-email">hello@coastalsagewellness.com</p>
      </address>
    </article>
  </main>
</body>
</html>
```